KalVeno Website- Joomla Template

A website for a Plumber company. A one page design ( this is what i mean http://vollantiwerk.example/en/#graph)
The website should be a template for Joomla, i will do the website in 3 languages
I want it to be elegant but not so that it looks like a consulting company.
My customers are private customers, my products are :
Main focus is on Fixing 24/7
then renovate bathrooms
replace heating systems
and Maintenance
I need 12 slides:
Who we are
News
Service
Maintenance
Renewable Energy
Sanitary
Heating
Ventilation
Partners
Useful Links
Contact us
of course a Facebook, twitter and G+ icon
try to make an innovative nice menu

```html
<!DOCTYPE html>
<html lang="en">
<head>
<meta charset="utf-8">
<title>KalVeno – Qualité par tradition</title>
<link href="https://fonts.googleapis.com/css2?family=Hind:wght@400;500&family=Cormorant+Garamond:wght@500&display=swap" rel="stylesheet">
<style>
:root{
  --green:#33b040;
  --green-text:#2aa83a;
  --navy:#134b86;
  --title-blue:#3f6fd0;
  --text:#3c3c3c;
  --muted:#555;
  --button:#9d8fd8;
  --white:#fff;
}
*{margin:0;padding:0;box-sizing:border-box}
html,body{width:1042px;height:1200px;overflow:hidden;background:var(--white)}
body{position:relative;font-family:"Hind",sans-serif;color:var(--text)}
.header{position:absolute;top:0;left:0;width:1042px;height:128px}
.brand{position:absolute;left:108px;top:36px;display:flex;align-items:center;gap:10px}
.brand-mark{width:44px;height:44px;border:4px solid var(--navy);border-radius:50%}
.brand-name{font-size:36px;font-weight:500;color:var(--navy);letter-spacing:1px}
.top-links{position:absolute;right:118px;top:20px;display:flex;gap:16px;font-size:13px;color:var(--green-text)}
.social{position:absolute;left:755px;top:71px;display:flex;gap:8px}
.social span{width:32px;height:32px;border-radius:6px;background:#9aa6b4}
.menu-toggle{position:absolute;left:891px;top:77px;width:32px;display:flex;flex-direction:column;gap:7px}
.menu-toggle span{height:4px;background:var(--navy);border-radius:1px}
.main-nav{position:absolute;top:128px;left:0;width:1042px;height:49px;background:var(--green);display:flex;align-items:center;padding-left:106px;gap:16.5px;font-size:13px;color:var(--white)}
.hero{position:absolute;top:177px;left:0;width:1042px;height:423px;background:linear-gradient(100deg,#d8d8d6 0%,#eeeeec 35%,#c9c7c3 60%,#b9aea4 100%)}
.hero-caption{position:absolute;left:226px;top:230px;width:590px;height:47px;background:rgba(40,40,40,.72);color:var(--white);font-family:"Cormorant Garamond",serif;font-weight:500;font-size:29px;word-spacing:14px;letter-spacing:.5px;display:flex;align-items:center;justify-content:center}
.services{position:absolute;top:612px;left:129px;display:flex;gap:6px}
.service{width:192px;height:126px;background:linear-gradient(#f4f4f4,#ececec);box-shadow:0 2px 3px rgba(0,0,0,.08);text-align:center;padding-top:10px;font-size:14.5px;line-height:19px;color:#333;position:relative}
.service svg{position:absolute;left:64px;top:50px}
.welcome{position:absolute;top:763px;left:0;width:1042px;text-align:center}
.section-title{font-family:"Cormorant Garamond",serif;font-weight:500;font-size:29px;color:var(--title-blue);letter-spacing:.5px}
.welcome p{margin:10px auto 0;width:800px;font-size:12.5px;line-height:17px;color:var(--muted)}
.read-more{display:inline-block;margin-top:16px;width:100px;height:31px;line-height:33px;background:var(--button);color:var(--white);font-size:14.5px;border-radius:3px}
.partners{position:absolute;top:900px;left:0;width:1042px;text-align:center}
.partner-row{position:absolute;left:0;width:1042px;display:flex;justify-content:center;gap:44px}
.partner-row span{width:82px;height:16px;background:#b3b3b3;border-radius:2px}
.footer-nav{position:absolute;top:1094px;left:0;width:1042px;text-align:center;font-size:13px;color:#333;line-height:29px}
.footer-nav div{display:flex;justify-content:center;gap:16.5px}
.footer-bar{position:absolute;top:1154px;left:0;width:1042px;height:46px;background:var(--green);text-align:center;line-height:50px;font-size:12.5px;color:#3a3a3a}
</style>
</head>
<body>
<header class="header">
  <div class="brand"><span class="brand-mark"></span><span class="brand-name">KalVeno</span></div>
  <div class="top-links"><span>Useful Links</span><span>Contact us</span></div>
  <div class="social" aria-label="Social networks"><span></span><span></span><span></span></div>
  <div class="menu-toggle" aria-label="Menu"><span></span><span></span><span></span></div>
</header>

<nav class="main-nav">
  <span>Home</span><span>Who we are</span><span>News</span><span>Service</span><span>Maintenance</span><span>Renewable Energy</span><span>Sanitary</span><span>Heating</span><span>Ventilation</span><span>Air Conditioning</span><span>Partners</span>
</nav>

<section class="hero" role="img" aria-label="Photo of a chrome kitchen tap over a white sink by a window with plants">
  <div class="hero-caption">KALVENO QUALITE PAR TRADITION</div>
</section>

<section class="services">
  <div class="service">Our Main focus is<br>on Fixing 24/7
    <svg width="64" height="64" viewBox="0 0 64 64"><circle cx="32" cy="32" r="32" fill="var(--navy)"/><circle cx="32" cy="32" r="18" fill="none" stroke="#fff" stroke-width="3"/><text x="32" y="37" text-anchor="middle" font-family="Hind,sans-serif" font-weight="500" font-size="15" fill="#fff">24</text></svg>
  </div>
  <div class="service">Renovate bathrooms
    <svg width="64" height="64" viewBox="0 0 64 64"><circle cx="32" cy="32" r="32" fill="var(--navy)"/><path d="M16 36a16 16 0 0 1 26-12z" fill="#fff"/><path d="M36 22q6-8 13-6" stroke="#fff" stroke-width="3" fill="none"/><g fill="#fff"><circle cx="20" cy="42" r="2"/><circle cx="27" cy="45" r="2"/><circle cx="34" cy="42" r="2"/><circle cx="23" cy="50" r="2"/><circle cx="31" cy="51" r="2"/></g></svg>
  </div>
  <div class="service">Replace heating systems
    <svg width="64" height="64" viewBox="0 0 64 64"><circle cx="32" cy="32" r="32" fill="var(--navy)"/><path d="M33 10c2 10 12 14 12 28a13 13 0 0 1-26 0c0-8 6-12 6-18 4 4 4 8 4 10 3-5 5-12 4-20z" fill="#fff"/><path d="M32 30c1 5 6 7 6 13a6 6 0 0 1-12 0c0-4 4-7 6-13z" fill="var(--navy)"/></svg>
  </div>
  <div class="service" style="padding-top:14px">Maintenance
    <svg width="64" height="64" viewBox="0 0 64 64"><circle cx="32" cy="32" r="32" fill="var(--navy)"/><path d="M18 46l16-16a8 8 0 0 1 10-10l-5 5 2 4 4 2 5-5a8 8 0 0 1-10 10L24 52z" fill="#fff"/><path d="M20 20l6 0 12 12-4 4-12-12z" fill="#fff"/></svg>
  </div>
</section>

<section class="welcome">
  <h2 class="section-title">WELCOME TEXT</h2>
  <p>Nemo enim ipsam voluptatem quia voluptas sit aspernatur aut odit aut fugit, sed quia consequuntur magni dolores eos qui ratione voluptatem sequi nesciunt. Neque porro quisquam est, qui dolorem ipsum quia dolor sit amet</p>
  <span class="read-more">Read more</span>
</section>

<section class="partners">
  <h2 class="section-title">PARTNERS</h2>
  <div class="partner-row" style="top:70px"><span></span><span></span><span></span><span></span><span></span></div>
  <div class="partner-row" style="top:132px"><span></span><span></span><span></span><span></span></div>
</section>

<footer class="footer-nav">
  <div><span>Home</span><span>Who we are</span><span>News</span><span>Service</span><span>Maintenance</span><span>Renewable Energy</span><span>Sanitary</span><span>Heating</span><span>Ventilation</span><span>Air Conditioning</span><span>Partners</span></div>
  <div><span>Useful Links</span><span>Contact Us</span><span>Privact policy</span><span>Terms &amp; Conditions</span></div>
</footer>
<div class="footer-bar">© 2014.www.companyname.com</div>
</body>
</html>
```